UI/UX Design for AI Photo-to-Video Web Platform (Figma)

I am looking for a modern, high-converting redesign for my Next.js-based web platform. The service allows users to transform old photos into vibrant memories using AI. The design needs to be clean, intuitive, and "mobile-ready" (responsive).
Key Features to Visualize on the Homepage:
Photo Restoration & Colorization: A clear "before/after" visual showing a black-and-white photo turning into a high-quality color photo.
Photo-to-Video Animation: A visual representation of how both B&W and color photos are transformed into dynamic video clips.
Story Creation: A section showing how these photos and videos are combined into a single "Story Video" with background music.
Scope of Work:
Homepage Redesign: A hero section with the core value proposition and a visual walkthrough of the process.
Service/Internal Pages: Redesigning the functional pages where users upload files and manage their projects.
Responsive Design: While the focus is desktop, the layout must be designed with a "Mobile-First" mindset for easy porting to a mobile app later.
Technical Requirements for the Designer:
Tool: Must be designed in Figma.
Structure: Use Figma Auto Layout and Components for all elements (buttons, inputs, cards).
Design System: Provide a clear style guide (Typography, Color Palette, Spacing).
Assets: All icons should be in SVG format.
Style Preference:
Modern, sleek, and trustworthy.
Since the product is about "memories," the vibe should be emotional yet technologically advanced (AI-driven).

```html
<!DOCTYPE html>
<html lang="en">
<head>
<meta charset="utf-8">
<title>Huebloom.ai — Images</title>
<link rel="stylesheet" href="https://fonts.googleapis.com/css2?family=Inter:wght@400;500;600;700&display=swap">
<style>
:root{
  --ink:#17171c;
  --muted:#55565e;
  --faint:#8a8b92;
  --line:#e4e4ea;
  --panel:#efeff3;
  --white:#ffffff;
  --accent:#8c9bf2;
  --accent-2:#b3a3ee;
  --pink:#eaa6d2;
  --orange:#f3a42a;
  --orange-text:#de7a0c;
  --red:#ee4a4a;
  --green:#2f9a55;
  --bw-dark:#2a2a2c;
  --bw-light:#9c9b98;
  --col-green:#4f7a3c;
  --col-blue:#2c3f86;
}
*{box-sizing:border-box;margin:0;padding:0}
html,body{width:1200px;height:988px;overflow:hidden}
body{
  font-family:"Inter",sans-serif;color:var(--ink);position:relative;
  background:
    radial-gradient(circle at 190px 270px, rgba(250,215,180,.55), transparent 210px),
    radial-gradient(circle at 1000px 170px, rgba(200,205,250,.55), transparent 260px),
    radial-gradient(circle at 230px 600px, rgba(210,215,250,.4), transparent 220px),
    radial-gradient(circle at 1020px 560px, rgba(250,225,205,.45), transparent 200px),
    #fbfbfd;
}
.topbar{height:63px;border-bottom:1px solid var(--line);position:relative;background:rgba(255,255,255,.6)}
.brand{position:absolute;left:24px;top:19px;font-size:17px;font-weight:600;letter-spacing:-.2px}
.nav{position:absolute;left:448px;top:14px;width:303px;height:34px;border:1px solid #d9dbf3;border-radius:18px;background:rgba(255,255,255,.7);display:flex;align-items:center;padding:2px;gap:6px}
.nav-item{display:flex;align-items:center;gap:6px;font-size:10.5px;font-weight:500;padding:0 10px;height:28px;border-radius:15px}
.nav-item.active{background:linear-gradient(90deg,var(--accent),var(--pink) 70%,#f2b58a);color:#fff;width:80px}
.nav-item svg{width:13px;height:13px}
.meter{position:absolute;top:19px;height:25px;border:1px solid #dcdcea;border-radius:13px;display:flex;align-items:center;gap:5px;padding:0 9px;font-size:10px;background:#fff}
.meter b{font-weight:600}
.meter span{color:var(--faint)}
.storage{left:868px;width:105px;border-color:#c6cdf3}
.credits{left:979px;width:94px}
.credit-dot{width:11px;height:11px;border-radius:50%;background:linear-gradient(135deg,var(--accent),var(--pink))}
.user{position:absolute;left:1085px;top:24px;font-size:10.5px;font-weight:600}
.avatar{position:absolute;left:1150px;top:19px;width:25px;height:25px;border-radius:50%;background:linear-gradient(135deg,#e8cbb8,#b98d74)}

.panel{position:absolute;left:245px;width:710px;background:rgba(238,238,243,.92);border-radius:16px;box-shadow:0 4px 14px rgba(80,80,110,.08)}
.panel-head{height:44px;position:relative;display:flex;align-items:center;padding:0 17px}
.panel-title{display:flex;align-items:center;gap:7px;font-size:13px;font-weight:600}
.panel-title svg{width:16px;height:16px}
.panel-note{position:absolute;left:0;right:0;text-align:center;font-size:9.5px;color:var(--muted);pointer-events:none}
.upload{top:95px;height:186px}
.btn-select{position:absolute;right:12px;top:9px;width:89px;height:25px;border-radius:8px;background:linear-gradient(90deg,var(--accent),var(--accent-2));color:#fff;font-size:9.5px;font-weight:600;display:flex;align-items:center;justify-content:center;gap:5px}
.dropzone-wrap{margin:0 5px;background:#fff;border-radius:12px;height:137px;padding:5px 6px}
.dropzone{border:1px dashed #c8c9d6;border-radius:10px;height:126px;display:flex;flex-direction:column;align-items:center;justify-content:center;gap:9px}
.dropzone h2{font-size:13.5px;font-weight:500}
.dropzone p{font-size:8.5px;color:var(--muted)}

.gallery{top:295px;height:605px}
.disclaimer{position:absolute;right:12px;display:flex;align-items:center;gap:5px;color:var(--orange-text);font-size:10px;font-weight:500}
.disclaimer i{width:12px;height:12px;border-radius:50%;background:var(--orange-text);color:#fff;font-style:normal;font-size:8px;font-weight:700;display:flex;align-items:center;justify-content:center}
.row{margin:0 5px 7px;background:#fff;border-radius:12px;height:181px;padding:6px;display:grid;grid-template-columns:175px 175px 175px 144px;gap:7px}
.tile{border-radius:10px;background:linear-gradient(90deg,var(--accent),var(--pink) 80%,#efb1a6);padding:0 1.5px 1.5px;position:relative;display:flex;flex-direction:column}
.tile-label{height:19px;font-size:8.5px;font-weight:500;color:#fff;padding:6px 0 0 11px}
.tile-body{flex:1;background:#fff;border-radius:9px 9px 8px 8px;position:relative;overflow:hidden;display:flex;flex-direction:column;align-items:center;justify-content:center;gap:8px;color:var(--faint);font-size:10px}
.shot{position:absolute;left:0;right:0;top:10px;height:129px}
.shot.bw{background:linear-gradient(160deg,var(--bw-light),#5d5c5a 45%,var(--bw-dark))}
.shot.bw-2{background:linear-gradient(150deg,#d6d4cf,#7a7874 40%,#242325)}
.shot.color{background:linear-gradient(155deg,var(--col-green),#7b6a4e 40%,var(--col-blue) 75%,#1c1d2b)}
.save{position:absolute;right:7px;bottom:7px;width:27px;height:27px;border-radius:8px;background:var(--orange);display:flex;align-items:center;justify-content:center}
.save svg{width:12px;height:12px}
.done{position:absolute;right:7px;top:15px;height:11px;padding:0 5px;border-radius:6px;background:var(--green);color:#fff;font-size:7px;font-weight:500;display:flex;align-items:center;gap:2px}
.spinner{width:20px;height:20px}
.actions{display:flex;flex-direction:column;justify-content:flex-end;gap:6px;padding-bottom:0}
.btn{height:25px;border-radius:8px;display:flex;align-items:center;position:relative;font-size:10px;font-weight:500;justify-content:center}
.btn svg{position:absolute;left:12px;width:11px;height:11px}
.btn-rotate{border:1px solid #cfd0d8;color:var(--ink)}
.btn-delete{border:1px solid var(--red);color:var(--red)}
.btn-generate{background:var(--orange);color:#fff;font-weight:600}
.timing{flex:1;border:1px solid var(--line);border-radius:10px;display:flex;flex-direction:column;align-items:center;justify-content:center;gap:4px}
.timing small{font-size:9.5px;color:var(--muted);margin-top:6px}
.timing strong{font-size:19px;font-weight:500}
</style>
</head>
<body>
<header class="topbar">
  <div class="brand">Huebloom.ai</div>
  <nav class="nav">
    <div class="nav-item active"><svg viewBox="0 0 16 16" fill="none" stroke="#fff" stroke-width="1.4"><rect x="2" y="2" width="12" height="12" rx="3"/><circle cx="6" cy="6" r="1.3"/><path d="M3 12l3.5-3.5 5 4"/></svg>Images</div>
    <div class="nav-item"><svg viewBox="0 0 16 16" fill="none" stroke="#17171c" stroke-width="1.4"><circle cx="8" cy="8" r="6.2"/><path d="M6.6 5.6l3.6 2.4-3.6 2.4z"/></svg>Video Animations</div>
    <div class="nav-item"><svg viewBox="0 0 16 16" fill="none" stroke="#17171c" stroke-width="1.4"><path d="M8 2a4 4 0 0 0-2.4 7.2V11h4.8V9.2A4 4 0 0 0 8 2zM6.3 13.5h3.4"/></svg>Studio</div>
  </nav>
  <div class="meter storage"><svg width="12" height="12" viewBox="0 0 16 16" fill="none" stroke="#8c9bf2" stroke-width="1.4"><path d="M4.5 12a3 3 0 0 1-.3-6 4 4 0 0 1 7.7 1 2.5 2.5 0 0 1 .1 5M8 8v6M6 10l2-2 2 2"/></svg><b>114 MB</b><span>/ 1.0 GB</span></div>
  <div class="meter credits"><div class="credit-dot"></div><b>4740</b><span>Credits</span></div>
  <div class="user">Mira Tolen</div>
  <div class="avatar" role="img" aria-label="User profile portrait"></div>
</header>

<section class="panel upload">
  <div class="panel-head">
    <div class="panel-title"><svg viewBox="0 0 16 16" fill="none" stroke="#8c9bf2" stroke-width="1.3"><path d="M4.5 12a3 3 0 0 1-.3-6 4 4 0 0 1 7.7 1 2.5 2.5 0 0 1 .1 5M8 8v6M6 10l2-2 2 2"/></svg>Upload Images</div>
    <div class="panel-note">Upload photos to generate vintage and real color versions.</div>
    <div class="btn-select"><svg width="11" height="11" viewBox="0 0 16 16" fill="none" stroke="#fff" stroke-width="1.4"><path d="M4 2h5l3 3v9H4zM9 2v3h3M8 12V8M6.5 9.5L8 8l1.5 1.5"/></svg>Select Files</div>
  </div>
  <div class="dropzone-wrap">
    <div class="dropzone">
      <h2>Drag and drop images here</h2>
      <p>Maximum 20 images • 100MB total • JPG, PNG, GIF, TIFF up to 10MB each</p>
    </div>
  </div>
</section>

<section class="panel gallery">
  <div class="panel-head">
    <div class="panel-title"><svg viewBox="0 0 16 16" fill="none" stroke="#8c9bf2" stroke-width="1.3"><rect x="2" y="2" width="12" height="12" rx="3"/><circle cx="6" cy="6" r="1.3"/><path d="M3 12l3.5-3.5 5 4"/></svg>Images</div>
    <div class="panel-note">Each row shows Original, Vintage Color, and Real Color.</div>
    <div class="disclaimer"><i>i</i>AI Disclaimer</div>
  </div>

  <div class="row">
    <div class="tile"><div class="tile-label">Original ID: OLO9YDY5</div><div class="tile-body">
      <div class="shot bw" role="img" aria-label="Black and white family portrait"></div>
      <div class="save"><svg viewBox="0 0 16 16" fill="none" stroke="#fff" stroke-width="1.6"><path d="M4 2h5l3 3v9H4zM8 7v5M6 10l2 2 2-2"/></svg></div>
    </div></div>
    <div class="tile"><div class="tile-label">Vintage</div><div class="tile-body">Not generated</div></div>
    <div class="tile"><div class="tile-label">Real</div><div class="tile-body">Not generated</div></div>
    <div class="actions">
      <div class="btn btn-rotate"><svg viewBox="0 0 16 16" fill="none" stroke="#17171c" stroke-width="1.5"><path d="M3.5 5.5A5.5 5.5 0 1 0 6 2.9M3.5 2.5v3h3"/></svg>Rotate</div>
      <div class="btn btn-delete"><svg viewBox="0 0 16 16" fill="#ee4a4a"><path d="M5.5 1.5h5v1.5H14v1.5H2V3h3.5zM3.5 5.5h9l-.8 9H4.3z"/></svg>Delete</div>
      <div class="btn btn-generate"><svg viewBox="0 0 16 16" fill="#fff"><path d="M9 1l1.3 4.2L14.5 6.5l-4.2 1.3L9 12 7.7 7.8 3.5 6.5l4.2-1.3zM3.5 10l.7 2 2 .7-2 .7-.7 2-.7-2-2-.7 2-.7z"/></svg>Generate (20)</div>
    </div>
  </div>

  <div class="row">
    <div class="tile"><div class="tile-label">Original ID: OLO9YDY5</div><div class="tile-body">
      <div class="shot bw" role="img" aria-label="Black and white family portrait"></div>
      <div class="save"><svg viewBox="0 0 16 16" fill="none" stroke="#fff" stroke-width="1.6"><path d="M4 2h5l3 3v9H4zM8 7v5M6 10l2 2 2-2"/></svg></div>
    </div></div>
    <div class="tile"><div class="tile-label">Vintage</div><div class="tile-body">
      <div class="shot color" role="img" aria-label="Vintage colorized family portrait"></div>
      <div class="done">✓ Done</div>
      <div class="save"><svg viewBox="0 0 16 16" fill="none" stroke="#fff" stroke-width="1.6"><path d="M4 2h5l3 3v9H4zM8 7v5M6 10l2 2 2-2"/></svg></div>
    </div></div>
    <div class="tile"><div class="tile-label">Real</div><div class="tile-body">
      <div class="shot color" role="img" aria-label="Real colorized family portrait"></div>
      <div class="done">✓ Done</div>
      <div class="save"><svg viewBox="0 0 16 16" fill="none" stroke="#fff" stroke-width="1.6"><path d="M4 2h5l3 3v9H4zM8 7v5M6 10l2 2 2-2"/></svg></div>
    </div></div>
    <div class="actions">
      <div class="timing">
        <svg class="spinner" viewBox="0 0 20 20" fill="none" stroke-width="1.3"><circle cx="10" cy="10" r="8.5" stroke="#b9c0f5"/><path d="M10 4a6 6 0 1 1-6 6" stroke="#e2a3cf"/></svg>
        <small>Generation time:</small>
        <strong>3m 2s</strong>
      </div>
      <div class="btn btn-delete"><svg viewBox="0 0 16 16" fill="#ee4a4a"><path d="M5.5 1.5h5v1.5H14v1.5H2V3h3.5zM3.5 5.5h9l-.8 9H4.3z"/></svg>Delete</div>
    </div>
  </div>

  <div class="row">
    <div class="tile"><div class="tile-label">Original ID: OLO9YDY5</div><div class="tile-body">
      <div class="shot bw-2" role="img" aria-label="Black and white photo of a man holding a child"></div>
      <div class="save"><svg viewBox="0 0 16 16" fill="none" stroke="#fff" stroke-width="1.6"><path d="M4 2h5l3 3v9H4zM8 7v5M6 10l2 2 2-2"/></svg></div>
    </div></div>
    <div class="tile"><div class="tile-label">Vintage</div><div class="tile-body">
      <svg class="spinner" viewBox="0 0 20 20" fill="none" stroke-width="1.3"><circle cx="10" cy="10" r="8.5" stroke="#b9c0f5"/><path d="M10 4a6 6 0 1 1-6 6" stroke="#e2a3cf"/></svg>Generating</div></div>
    <div class="tile"><div class="tile-label">Real</div><div class="tile-body">
      <svg class="spinner" viewBox="0 0 20 20" fill="none" stroke-width="1.3"><circle cx="10" cy="10" r="8.5" stroke="#b9c0f5"/><path d="M10 4a6 6 0 1 1-6 6" stroke="#e2a3cf"/></svg>Generating</div></div>
    <div class="actions">
      <div class="btn btn-delete"><svg viewBox="0 0 16 16" fill="#ee4a4a"><path d="M5.5 1.5h5v1.5H14v1.5H2V3h3.5zM3.5 5.5h9l-.8 9H4.3z"/></svg>Delete</div>
    </div>
  </div>
</section>
</body>
</html>
```